4 x Designs Required

Hi There,
I require 4 x different designs to be made for 4 new brands of mine however they can be quite interchangeable. HR Plinkr and Marketing Plinkr can be similar just with a difference in colour. The same goes for the Bulletin brands. This means there are ultimately two designs that need perfecting.

There must be a click here CTA on the banner somewhere. :-)

I require the banners in 728x90 format and 960x90 please.

Please use strap lines on the banners such as:
Essential Whitepapers for HR Professionals
Essential Whitepapers for Marketing Professionals
Your No.1 Whitepaper Resource

The brand names:
HR Plinkr
Marketing Plinkr
HR Dispatchly
Marketing Dispatchly

Examples attached.

```html
<!DOCTYPE html>
<html lang="en">
<head>
<meta charset="utf-8">
<title>Whitepaper Banner Set</title>
<link href="https://fonts.googleapis.com/css2?family=Poppins:wght@500;600;700;800;900&display=swap" rel="stylesheet">
<style>
  :root {
    --stage: #6bbde2;
    --hr-navy-1: #0f2347;
    --hr-navy-2: #1b3f72;
    --hr-cyan: #19d3ef;
    --mk-brown-1: #231a1a;
    --mk-brown-2: #33262a;
    --mk-gold: #c9a06b;
    --bl-navy-1: #07182b;
    --bl-navy-2: #123454;
    --bl-flat: #08192c;
    --bl-green: #1fae4f;
    --bl-green-soft: #26b36c;
    --ink-dark: #15203a;
    --white: #ffffff;
  }
  * { margin: 0; padding: 0; box-sizing: border-box; }
  html, body { width: 1200px; height: 660px; overflow: hidden; }
  body {
    background: var(--stage);
    font-family: "Poppins", sans-serif;
    position: relative;
  }
  .banner {
    position: absolute;
    left: 98px;
    width: 1002px;
    height: 123px;
    overflow: hidden;
    color: var(--white);
  }
  .banner--hr-plinkr { top: 50px; background: radial-gradient(ellipse at 85% 30%, var(--hr-navy-2), var(--hr-navy-1) 65%); }
  .banner--mk-plinkr { top: 190px; background: linear-gradient(90deg, var(--mk-brown-1), var(--mk-brown-2)); }
  .banner--hr-dispatchly { top: 338px; background: radial-gradient(ellipse at 65% 20%, var(--bl-navy-2), var(--bl-navy-1) 70%); }
  .banner--mk-dispatchly { top: 487px; background: var(--bl-flat); }

  .brand-name {
    position: absolute;
    top: 50%;
    transform: translateY(-50%);
    font-weight: 800;
    line-height: 1;
    letter-spacing: -0.5px;
    text-transform: uppercase;
  }
  .banner--hr-plinkr .brand-name { left: 19px; font-size: 50px; color: var(--white); }
  .banner--mk-plinkr .brand-name { left: 29px; font-size: 27px; color: var(--mk-gold); }
  .banner--hr-dispatchly .brand-name { left: 24px; font-size: 30px; color: var(--white); }
  .banner--mk-dispatchly .brand-name { left: 19px; font-size: 30px; line-height: 1.05; color: var(--bl-green-soft); }

  .strapline {
    position: absolute;
    transform: translateX(-50%);
    text-align: center;
    text-transform: uppercase;
    line-height: 1;
  }
  .strapline__lead { display: block; font-weight: 800; }
  .strapline__main { display: block; font-weight: 800; letter-spacing: -0.5px; }
  .strapline__sub { display: block; font-weight: 600; letter-spacing: 2.6px; }

  .banner--hr-plinkr .strapline { left: 517px; top: 20px; }
  .banner--hr-plinkr .strapline__lead { font-size: 30px; color: var(--hr-cyan); }
  .banner--hr-plinkr .strapline__main { font-size: 42px; margin-top: -2px; }
  .banner--hr-plinkr .strapline__sub { font-size: 14px; color: var(--hr-cyan); margin-top: 0; }

  .banner--mk-plinkr .strapline { left: 563px; top: 17px; }
  .banner--mk-plinkr .strapline__lead { font-size: 32px; color: var(--mk-gold); }
  .banner--mk-plinkr .strapline__main { font-size: 47px; margin-top: -4px; }
  .banner--mk-plinkr .strapline__sub { font-size: 14px; color: var(--mk-gold); letter-spacing: 2px; margin-top: -1px; }

  .pointer-arrow { position: absolute; }
  .banner--hr-plinkr .pointer-arrow { left: 690px; top: 46px; width: 104px; height: 40px; }
  .banner--mk-plinkr .pointer-arrow { left: 746px; top: 38px; width: 112px; height: 46px; }

  .cta {
    position: absolute;
    display: flex;
    align-items: center;
    justify-content: center;
    text-transform: uppercase;
    font-weight: 700;
    text-decoration: none;
  }
  .cta--pill-cyan {
    left: 809px; top: 27px; width: 180px; height: 48px;
    border-radius: 24px;
    background: var(--hr-cyan);
    color: var(--ink-dark);
    font-size: 21px;
    box-shadow: 0 4px 0 rgba(0,0,0,0.25);
  }
  .cta--disc-gold {
    left: 878px; top: -10px; width: 150px; height: 143px;
    border-radius: 50%;
    background: var(--mk-gold);
    color: var(--mk-brown-1);
    font-size: 32px;
    line-height: 1.05;
    font-weight: 800;
    justify-content: flex-start;
    padding-left: 14px;
    text-align: left;
  }
  .cta--pill-green {
    width: 181px; height: 50px;
    border-radius: 25px;
    color: var(--white);
    font-size: 21px;
    box-shadow: 0 4px 0 rgba(0,0,0,0.3);
  }
  .banner--hr-dispatchly .cta--pill-green { left: 800px; top: 37px; background: var(--bl-green); }
  .banner--mk-dispatchly .cta--pill-green { left: 800px; top: 37px; background: var(--bl-green-soft); }

  .resource-line {
    position: absolute;
    top: 50%;
    transform: translateY(-50%);
    display: flex;
    align-items: center;
    text-transform: uppercase;
    font-weight: 900;
  }
  .banner--hr-dispatchly .resource-line { left: 322px; }
  .banner--mk-dispatchly .resource-line { left: 314px; }
  .resource-line__your {
    writing-mode: vertical-rl;
    transform: rotate(180deg);
    font-size: 14px;
    font-weight: 800;
    letter-spacing: 1px;
    color: var(--white);
    margin-right: 2px;
  }
  .resource-line__rank {
    font-size: 64px;
    line-height: 1;
    letter-spacing: -2px;
    color: var(--bl-green);
  }
  .banner--mk-dispatchly .resource-line__rank,
  .banner--mk-dispatchly .resource-line__word--accent { color: var(--bl-green-soft); }
  .resource-line__words { margin-left: 6px; display: flex; flex-direction: column; }
  .resource-line__word { font-size: 29px; line-height: 0.95; letter-spacing: -0.5px; color: var(--white); }
  .resource-line__word--accent { font-size: 33px; color: var(--bl-green); }
</style>
</head>
<body>

<section class="banner banner--hr-plinkr" role="img" aria-label="HR Plinkr banner on deep navy with a faint network-line backdrop">
  <div class="brand-name">HR Plinkr</div>
  <div class="strapline">
    <span class="strapline__lead">Essential</span>
    <span class="strapline__main">Whitepapers</span>
    <span class="strapline__sub">For HR Professionals</span>
  </div>
  <svg class="pointer-arrow" viewBox="0 0 104 40" fill="none" stroke="#ffffff" stroke-width="2" stroke-linecap="round" stroke-linejoin="round">
    <path d="M2 30 C 25 38, 45 34, 55 22 C 62 12, 54 6, 50 14 C 46 24, 70 24, 98 12"/>
    <path d="M88 8 L98 12 L92 21"/>
  </svg>
  <a class="cta cta--pill-cyan" href="#">Click Here</a>
</section>

<section class="banner banner--mk-plinkr">
  <div class="brand-name">Marketing Plinkr</div>
  <div class="strapline">
    <span class="strapline__lead">Essential</span>
    <span class="strapline__main">Whitepapers</span>
    <span class="strapline__sub">For Marketing Professionals</span>
  </div>
  <svg class="pointer-arrow" viewBox="0 0 112 46" fill="none" stroke="#ffffff" stroke-width="2" stroke-linecap="round" stroke-linejoin="round">
    <path d="M2 36 C 28 44, 48 40, 58 26 C 66 14, 56 8, 52 17 C 48 28, 76 28, 106 12"/>
    <path d="M96 8 L106 12 L100 21"/>
  </svg>
  <a class="cta cta--disc-gold" href="#">Click<br>Here</a>
</section>

<section class="banner banner--hr-dispatchly" role="img" aria-label="HR Dispatchly banner on dark navy with a faint glowing network backdrop">
  <div class="brand-name">HR Dispatchly</div>
  <div class="resource-line">
    <span class="resource-line__your">Your</span>
    <span class="resource-line__rank">No.1</span>
    <span class="resource-line__words">
      <span class="resource-line__word">Whitepaper</span>
      <span class="resource-line__word resource-line__word--accent">Resource</span>
    </span>
  </div>
  <a class="cta cta--pill-green" href="#">Click Here</a>
</section>

<section class="banner banner--mk-dispatchly">
  <div class="brand-name">Marketing<br>Dispatchly</div>
  <div class="resource-line">
    <span class="resource-line__your">Your</span>
    <span class="resource-line__rank">No.1</span>
    <span class="resource-line__words">
      <span class="resource-line__word">Whitepaper</span>
      <span class="resource-line__word resource-line__word--accent">Resource</span>
    </span>
  </div>
  <a class="cta cta--pill-green" href="#">Click Here</a>
</section>

</body>
</html>
```